Book Cover Design Project

NOTE. I need the design in four days of posting this!

This will be the cover of my first book, WALK THE HIGH LINE -
alchemy in the real business world. The book explains defines what Purpose and Meaning is, and how to use it in business. I have included the first chapter to provide a background.

I want the core colours to be black and white, and use the colours Violet, Cerulean Blue Extra Pale (powder blue), Cadmium Lemon (flouro yellow). I plan on using this design as the basis for future books in the WALK THE HIGH LINE series, where the yellow is carried through but the violet and blue colours changing.

This is a spiritual business book without using any spiritual language. It is strongly masculine and direct in its nature.

What I am looking for is something Remarkable that captures my reader immediately. My reader is a seeker. He/she is an entrepreneur perhaps looking to setup a new venture and looking for new and better ways of doing things, or he/she may be a small/medium business owner perhaps bored looking for more meaning in personal and business life), or the corporate person who is looking to get out and do something new. Age 35-50.
Updates

Hi I want to correct the paper size. It is "C Format" (trade paperbacks) are 135mm x 216mm (5.32" x 8.51").

Thks

Reason: A deadline has changed which means the completion of this book cover is less time-critical.

This is a business book that introduces new concepts, such as Purpose. Although it is based on spiritual principals  it is using normal business language when explaining what Purpose is, and how businesses can identify it and use it to be more successful.

If there is a border between a self-help and a business book, this book sits close to the border but markedly on the business side.

Hi I want to confirm the book size. The book size I require is the Australian C Format, which measures 153mm W x 234mm H. 

Sorry for any confusion

Reason: Hi I have extended the deadline as I want to be able to print prospective covers and see how they look like in a bookshop next to other covers.

Reason: To allow for final negotiations.

Industry/Entity Type

Business

```html
<!DOCTYPE html>
<html lang="en">
<head>
<meta charset="utf-8">
<title>Walk the High Line — Book Cover</title>
<link rel="stylesheet" href="https://fonts.googleapis.com/css2?family=Oswald:wght@300&family=Raleway:wght@400&family=Open+Sans:ital,wght@1,700&display=swap">
<style>
  :root {
    --page-bg: #ffffff;
    --ink-white: #ffffff;
    --deep-blue: #1d3f6e;
    --cerulean: #2f8fb3;
    --teal: #3b8f8a;
    --lemon: #d6d928;
    --moss: #7fa23a;
    --band-grey: rgba(70, 74, 80, 0.82);
  }
  html, body {
    margin: 0;
    padding: 0;
    width: 1200px;
    height: 900px;
    overflow: hidden;
    background: var(--page-bg);
  }
  .stage {
    position: relative;
    width: 1200px;
    height: 900px;
    display: flex;
    align-items: center;
    justify-content: center;
  }
  .cover {
    position: relative;
    width: 523px;
    height: 800px;
    overflow: hidden;
  }
  .cover-texture {
    position: absolute;
    inset: 0;
    background:
      radial-gradient(ellipse 70% 35% at 55% 72%, rgba(214, 217, 40, 0.85), rgba(214, 217, 40, 0) 70%),
      radial-gradient(ellipse 60% 30% at 80% 45%, rgba(200, 210, 60, 0.55), rgba(200, 210, 60, 0) 70%),
      linear-gradient(180deg, var(--deep-blue) 0%, var(--cerulean) 25%, #4aa3b0 42%, var(--moss) 62%, var(--lemon) 75%, var(--teal) 92%, #2c6f86 100%);
  }
  .author-name {
    position: absolute;
    top: 52px;
    left: 0;
    right: 0;
    text-align: center;
    font-family: "Raleway", sans-serif;
    font-weight: 400;
    font-size: 42px;
    letter-spacing: 0.16em;
    color: var(--ink-white);
    margin: 0;
  }
  .book-title {
    position: absolute;
    top: 176px;
    left: 26px;
    margin: 0;
    font-family: "Oswald", sans-serif;
    font-weight: 300;
    font-size: 128px;
    line-height: 134px;
    color: var(--ink-white);
    text-transform: uppercase;
    letter-spacing: 0.01em;
    white-space: nowrap;
  }
  .book-title span { display: block; }
  .subtitle-band {
    position: absolute;
    top: 604px;
    left: 14px;
    right: 14px;
    height: 40px;
    background: var(--band-grey);
    border-top: 3px solid var(--ink-white);
    display: flex;
    align-items: center;
    justify-content: center;
  }
  .subtitle {
    margin: 0;
    font-family: "Open Sans", sans-serif;
    font-style: italic;
    font-weight: 700;
    font-size: 23px;
    letter-spacing: 0.04em;
    color: var(--ink-white);
  }
</style>
</head>
<body>
  <main class="stage">
    <section class="cover">
      <div class="cover-texture" role="img" aria-label="Grunge painted wall texture in deep blue, cerulean and lemon yellow"></div>
      <p class="author-name">AUTHOR NAME</p>
      <h1 class="book-title"><span>Walk</span><span>The High</span><span>Line</span></h1>
      <div class="subtitle-band">
        <p class="subtitle">Alchemy in the Real Business World</p>
      </div>
    </section>
  </main>
</body>
</html>
```